Stationery Design Project

We are a packaging machinery manufacturer that mainly serve the food industry.
We now require a full set of stationary including name card, envelop, letter paper, and etc. to match our company image. The logo has been awarded in a previous contest which is attached here.
Updates
Project Deadline Extended
Reason: We have extended the deadline. We have adjusted the deadline before launch to avoid confusion but it turns out the new date wasn't implemented by the system. All designers please feel free to submit your design. Thank you!
Target Market(s)
B2B customer, including decision maker in food factories, chemical factories, etc.
Industry/Entity Type
Industry
Colors
Designer to choose colors to be used in the design.
Look and feel
Each slider illustrates characteristics of the customer's brand and the style your logo design should communicate.

```html
<!DOCTYPE html>
<html lang="en">
<head>
<meta charset="utf-8">
<title>Vortane Packaging Technology – Business Card</title>
<link rel="stylesheet" href="https://fonts.googleapis.com/css2?family=Archivo:wght@700;800&family=Questrial&display=swap">
<style>
  :root{
    --brand-green:#046a38;
    --slate:#7f868c;
    --pale-grey:#d9dcdd;
    --paper:#f7f8f8;
    --backdrop:#e9e9ec;
    --ink:#4a4d50;
    --white:#ffffff;
  }
  *{box-sizing:border-box;margin:0;padding:0}
  html,body{width:1200px;height:934px;overflow:hidden}
  body{background:var(--backdrop);position:relative;font-family:"Questrial",sans-serif}

  .card{position:absolute;width:640px;height:366px;overflow:hidden;box-shadow:0 2px 6px rgba(0,0,0,.12)}
  .card-front{left:60px;top:70px;background:var(--brand-green)}
  .card-back{left:500px;top:498px;background:var(--paper)}
  .corner-chevron{position:absolute;left:0;top:0;width:640px;height:366px}

  .wordmark{position:absolute;left:70px;font-family:"Archivo",sans-serif;font-weight:800;font-size:62px;letter-spacing:2px;line-height:1}
  .tagline{position:absolute;left:72px;font-family:"Archivo",sans-serif;font-weight:700;font-size:15px;letter-spacing:3.6px}
  .card-front .wordmark{top:118px;color:var(--white)}
  .card-front .tagline{top:186px;color:var(--white)}
  .website{position:absolute;left:72px;top:286px;color:var(--white);font-size:17px;letter-spacing:.5px}
  .website b{font-family:"Archivo",sans-serif;font-weight:700}

  .card-back .wordmark{top:108px;color:var(--brand-green)}
  .card-back .tagline{top:176px;color:var(--slate)}

  .holder{position:absolute;right:58px;top:182px;text-align:left}
  .holder-name{font-family:"Archivo",sans-serif;font-weight:700;font-size:21px;color:var(--ink);letter-spacing:.5px}
  .holder-role{font-size:15px;color:var(--brand-green);margin-top:2px}

  .bar{position:absolute;height:7px}
  .bar-slate{left:468px;top:238px;width:132px;background:var(--slate)}
  .bar-green-top{left:210px;top:246px;width:248px;background:var(--brand-green)}
  .bar-green-bottom{left:70px;top:320px;width:300px;background:var(--brand-green)}

  .contacts{position:absolute;left:70px;top:268px;font-size:15px;color:var(--ink);line-height:21px;list-style:none}
  .contacts b{color:var(--brand-green);font-family:"Archivo",sans-serif;font-weight:700}
  .contacts .sep{margin:0 6px;color:var(--ink)}
</style>
</head>
<body>

<section class="card card-front" aria-label="Business card front">
  <svg class="corner-chevron" viewBox="0 0 640 366" aria-hidden="true">
    <polygon points="500,0 640,0 640,180 430,55" fill="var(--white)"/>
    <polygon points="545,0 640,0 640,112 505,38" fill="var(--slate)"/>
  </svg>
  <div class="wordmark">VORTANE</div>
  <div class="tagline">PACKAGING TECHNOLOGY</div>
  <p class="website">www.<b>vortane</b>.com</p>
</section>

<section class="card card-back" aria-label="Business card back">
  <svg class="corner-chevron" viewBox="0 0 640 366" aria-hidden="true">
    <polygon points="455,0 525,0 495,42 640,128 640,182 415,50" fill="var(--pale-grey)"/>
  </svg>
  <div class="wordmark">VORTANE</div>
  <div class="tagline">PACKAGING TECHNOLOGY</div>

  <div class="holder">
    <p class="holder-name">MARA ELLISON</p>
    <p class="holder-role">Managing Director</p>
  </div>

  <div class="bar bar-slate"></div>
  <div class="bar bar-green-top"></div>

  <ul class="contacts">
    <li><b>T:</b> +91-11-40208866<span class="sep">·</span><b>F:</b> +91-11-40208877</li>
    <li><b>M:</b> +91-11-40208866<span class="sep">·</span><b>E:</b> info@vortane.com</li>
  </ul>

  <div class="bar bar-green-bottom"></div>
</section>

</body>
</html>
```